Web Meeting Company Needs Bullet Point Icons for Power Point Presentation

I need 6 Icons / Buttons built to place into a power point presentation.

I have attached 2 slides. The first slide has the exsisting icons that we are using. On the next slide we need Icons that look similar to those in slide one, but reflect the discriptions that are listed next to the current Icons.

- Crowd Sourcing
- Kick Starters
- Segmentation
- Build A...
- Pop-Ups
- Gamification

On Slide 2 I have also uploaded a screen shot of some icons from GlimmerVault that i think would work from a symbol standpoint

Target Market(s)

Pharma Meeting Planning

Industry/Entity Type

It Company

Requirements
Must have
• Icons
Nice to have
• Icons
Should not have
• Icons

```html
<!DOCTYPE html>
<html lang="en">
<head>
<meta charset="utf-8">
<title>Audience Engagement Themes</title>
<link href="https://fonts.googleapis.com/css2?family=Arimo:wght@400;700&display=swap" rel="stylesheet">
<style>
  :root {
    --title-purple: #b0399f;
    --label-orange: #f0902a;
    --orange: #f39c3a;
    --orange-deep: #dd7a22;
    --purple: #b33aa5;
    --purple-deep: #8c2983;
    --teal: #4fc7d8;
    --teal-deep: #22a6bc;
    --band: #4bc3d2;
    --brand-grey: #7b7b7b;
    --paper: #ffffff;
  }
  * { margin: 0; padding: 0; box-sizing: border-box; }
  html, body { width: 1200px; height: 900px; overflow: hidden; background: var(--paper); }
  .slide {
    position: relative;
    width: 1200px;
    height: 900px;
    font-family: "Arimo", Arial, sans-serif;
    background: var(--paper);
    overflow: hidden;
  }
  .backdrop-texture {
    position: absolute;
    top: 0; right: 0;
    width: 640px; height: 620px;
    background: radial-gradient(ellipse at 85% 30%, #efefef 0%, #f6f6f6 45%, rgba(255,255,255,0) 75%);
  }
  .slide-title {
    position: absolute;
    left: 67px; top: 78px;
    font-size: 40px;
    font-weight: 400;
    color: var(--title-purple);
    letter-spacing: 0.2px;
  }
  .theme-list { list-style: none; }
  .theme {
    position: absolute;
    left: 66px;
    display: flex;
    align-items: center;
    height: 90px;
  }
  .theme-icon { width: 90px; height: 90px; flex: none; }
  .theme-label {
    margin-left: 17px;
    font-size: 24px;
    font-weight: 700;
    color: var(--label-orange);
  }
  .brand {
    position: absolute;
    left: 928px; top: 768px;
    display: flex;
    align-items: center;
    gap: 12px;
  }
  .brand-name {
    font-size: 56px;
    font-weight: 700;
    color: var(--brand-grey);
    letter-spacing: -1px;
  }
  .brand-square { width: 34px; height: 34px; background: var(--purple); }
  .footer-band {
    position: absolute;
    left: 0; bottom: 0;
    width: 1200px; height: 49px;
    background: var(--band);
  }
  .footer-notch {
    position: absolute;
    left: 129px; top: 0;
    width: 0; height: 0;
    border-left: 10px solid transparent;
    border-right: 10px solid transparent;
    border-top: 10px solid var(--paper);
  }
</style>
</head>
<body>
<div class="slide">
  <div class="backdrop-texture" role="img" aria-label="Faint repeating geometric background texture"></div>

  <h1 class="slide-title">Audience Engagement Themes</h1>

  <svg width="0" height="0" style="position:absolute">
    <defs>
      <clipPath id="disc"><circle cx="45" cy="45" r="45"/></clipPath>
    </defs>
  </svg>

  <ul class="theme-list">
    <li class="theme" style="top:177px">
      <svg class="theme-icon" viewBox="0 0 90 90" aria-hidden="true">
        <circle cx="45" cy="45" r="45" fill="var(--orange)"/>
        <polygon clip-path="url(#disc)" points="18,48 72,48 110,86 110,110 56,110" fill="var(--orange-deep)"/>
        <rect x="16" y="26" width="58" height="24" rx="12" fill="#fff"/>
        <circle cx="30" cy="36" r="4" fill="var(--orange)"/>
        <path d="M22 46 a8 6 0 0 1 16 0z" fill="var(--orange)"/>
        <circle cx="60" cy="36" r="4" fill="var(--orange)"/>
        <path d="M52 46 a8 6 0 0 1 16 0z" fill="var(--orange)"/>
        <circle cx="45" cy="33" r="5.5" fill="var(--orange)"/>
        <path d="M34 48 a11 8 0 0 1 22 0z" fill="var(--orange)"/>
      </svg>
      <span class="theme-label">Crowd Sourcing</span>
    </li>

    <li class="theme" style="top:286px">
      <svg class="theme-icon" viewBox="0 0 90 90" aria-hidden="true">
        <circle cx="45" cy="45" r="45" fill="var(--purple)"/>
        <polygon clip-path="url(#disc)" points="66,38 66,68 30,68 72,110 110,110 110,72" fill="var(--purple-deep)"/>
        <rect x="17" y="42" width="9" height="26" fill="#fff"/>
        <path d="M30 42 L42 28 L44 14 Q50 12 52 20 L50 36 L64 36 Q70 38 67 44 Q71 47 66 51 Q70 54 65 58 Q68 62 62 66 L30 66z" fill="#fff"/>
      </svg>
      <span class="theme-label">Kick Starters</span>
    </li>

    <li class="theme" style="top:396px">
      <svg class="theme-icon" viewBox="0 0 90 90" aria-hidden="true">
        <circle cx="45" cy="45" r="45" fill="var(--teal)"/>
        <polygon clip-path="url(#disc)" points="70,50 50,72 90,110 110,90" fill="var(--teal-deep)"/>
        <g fill="#fff">
          <path d="M45 45 L35 20 Q45 14 55 20z"/>
          <path d="M45 45 L62 24 Q72 30 72 40z"/>
          <path d="M45 45 L72 50 Q70 62 62 66z"/>
          <path d="M45 45 L55 70 Q45 76 35 70z"/>
          <path d="M45 45 L28 66 Q18 60 18 50z"/>
          <path d="M45 45 L18 40 Q20 28 28 24z"/>
        </g>
      </svg>
      <span class="theme-label">Segmentation</span>
    </li>

    <li class="theme" style="top:513px">
      <svg class="theme-icon" viewBox="0 0 90 90" aria-hidden="true">
        <circle cx="45" cy="45" r="45" fill="var(--orange)"/>
        <polygon clip-path="url(#disc)" points="26,68 70,68 110,108 110,110 66,110" fill="var(--orange-deep)"/>
        <g fill="#fff">
          <path d="M20 26 Q26 16 36 22 L32 28 L36 32 L42 28 Q46 38 38 42 L64 66 L60 70 L34 46 Q24 50 20 40 L26 36 L22 32z"/>
          <path d="M48 20 L62 16 L72 26 L66 30 L62 28 L30 66 L24 62 L56 28z"/>
        </g>
      </svg>
      <span class="theme-label">Build a…</span>
    </li>

    <li class="theme" style="top:619px">
      <svg class="theme-icon" viewBox="0 0 90 90" aria-hidden="true">
        <circle cx="45" cy="45" r="45" fill="var(--purple)"/>
        <polygon clip-path="url(#disc)" points="60,40 66,60 50,74 86,110 110,110 110,70" fill="var(--purple-deep)"/>
        <path d="M45 74 Q24 72 24 54 Q24 42 34 34 Q34 42 38 44 Q38 28 50 16 Q50 28 58 36 Q62 30 60 24 Q68 34 66 54 Q66 72 45 74z" fill="#fff"/>
        <path d="M45 68 Q36 66 37 58 Q38 52 44 46 Q44 52 48 54 Q52 52 52 48 Q55 54 54 60 Q53 66 45 68z" fill="var(--purple)"/>
      </svg>
      <span class="theme-label">Pop Ups</span>
    </li>

    <li class="theme" style="top:727px">
      <svg class="theme-icon" viewBox="0 0 90 90" aria-hidden="true">
        <circle cx="45" cy="45" r="45" fill="var(--teal)"/>
        <polygon clip-path="url(#disc)" points="68,58 30,70 66,110 110,110 110,84" fill="var(--teal-deep)"/>
        <path d="M46 36 Q46 26 52 24 Q56 22 56 16" stroke="#fff" stroke-width="3" fill="none"/>
        <path d="M26 36 L64 36 Q74 36 74 50 Q74 66 66 66 Q60 66 56 58 L34 58 Q30 66 24 66 Q16 66 16 50 Q16 36 26 36z" fill="#fff"/>
        <g fill="var(--teal)">
          <rect x="23" y="45" width="11" height="3"/>
          <rect x="27" y="41" width="3" height="11"/>
          <circle cx="58" cy="42" r="2"/>
          <circle cx="58" cy="52" r="2"/>
          <circle cx="53" cy="47" r="2"/>
          <circle cx="63" cy="47" r="2"/>
          <rect x="38" y="50" width="5" height="2"/>
          <rect x="46" y="50" width="5" height="2"/>
        </g>
      </svg>
      <span class="theme-label">Gamification</span>
    </li>
  </ul>

  <div class="brand">
    <span class="brand-name">quorvel</span>
    <span class="brand-square"></span>
  </div>

  <div class="footer-band"><span class="footer-notch"></span></div>
</div>
</body>
</html>
```